Bi Fold Brochure for #1 New Release Book - Ride Onward, by Hall of Fame cowboy Dalton Prewitt.

I need a bi-fold brochure (printed front and back) to give away at marketing events to increase awareness and ultimately gain pre-orders for my upcoming book. Im thinking 8x5x11 overall size, folded in half but am open to other standard sizes. Not only do I want people have a quality brochure in their hands, I want it to inspire them to pre-order the book, follow my social media pages, visit my website (www.daltonprewitt.example), etc. Attached is the word doc to be included to give readers a sampling of the book, along with a word doc with endorsements of what others are saying, as well as bookstore logos. Lastly, Brightwell and Tumbleford are proud partners in this endeavor so I'd like to include their logos as well. The final design should communicate professional, published author, credibility, relatable, yet compel the reader to buy the book.
Ride Onward stands for "Rise, Observe, Nurture, Aid, Rejoice, & Dedicate" so if that can be incorporated as well so it gives meaning to the title.
Updates

Any call to action for pre ordering Ride Onward would be ideal - I want the readers of this brochure to pick it up and be impressed by the quality and professionalism then be inspired to take action by ordering the book.I'd like to highlight what RIDE ONWARD means (Rise, Observe, Nurture, Aid, Rejoice, & Dedicate) Added Sunday, October 2, 2016

Project Deadline Extended Reason: Allowing more time for designers to submit designs - I have been notified that other designers have saved the project and are intending to submit so I want to allow adequate time for quality submissions. Thank you. Added Monday, October 3, 2016

Target Market(s)

Cowboys, Western Enthusiast, Christian Cowboys...but I do not want a western themed brochure. I want something appeals to a broader audience.

Industry/Entity Type

Book Publisher

Requirements
Must have
• Book Cover file
• Inside, I want the text from the actual book so readers get a sampling of the book
• Book Endorsement Statements (not sure if you can use all of them, but I want enough to make the point that others praise the book)
• Store Logos (Hartley & Crane, Velmora, Brightwell, Pages Galore), Social Media Logos, Partner Logos (Tumbleford, Brightwell) email: dprewitt07@mailnest.example
• Must have what Ride Onward stands for in a way that is appealing (Rise, Observe, Nurture, Aid, Rejoice, & Dedicate)
Nice to have
• Nice to have a theme that flows throughout the brochure - would like to use a color scheme that compliments the book cover. I'd like to mix the fonts...maybe Serif for the Headings and Sans Serif for the text of the book and endorsement statements. Incorporate photos where it makes most impact as well as the Hall of Fame file to add credibility.

```html
<!DOCTYPE html>
<html lang="en">
<head>
<meta charset="utf-8">
<title>Ride Onward – Bi-Fold Brochure</title>
<link href="https://fonts.googleapis.com/css2?family=Black+Ops+One&family=Crimson+Text:ital,wght@0,400;0,600;1,400;1,600&family=Oswald:wght@500;700&family=Roboto+Condensed:ital,wght@0,400;0,700;1,700&display=swap" rel="stylesheet">
<style>
:root{
  --stage:#c9c9c9;
  --paper:#171717;
  --paper-deep:#0e0e0e;
  --frame:#b8782a;
  --orange:#f39a1f;
  --gold:#c99a3a;
  --text:#d9d4cb;
  --muted:#9c958b;
  --photo-a:#3b3a36;
  --photo-b:#1c1b19;
}
*{box-sizing:border-box;margin:0;padding:0}
html,body{width:985px;height:1200px;overflow:hidden;background:var(--stage)}
body{position:relative;font-family:"Crimson Text",Georgia,serif;color:var(--text)}
.spread{position:absolute;left:62px;width:860px;height:556px;display:flex;box-shadow:0 6px 18px rgba(0,0,0,.35)}
.spread--outside{top:29px}
.spread--inside{top:614px}
.page{position:relative;width:430px;height:556px;background:linear-gradient(160deg,#222 0%,var(--paper) 55%,var(--paper-deep) 100%);overflow:hidden}
.page+.page{border-left:1px solid #000}
.frame{position:absolute;inset:12px;border:1px solid var(--frame);pointer-events:none}
.photo{position:absolute;background:linear-gradient(170deg,var(--photo-a),var(--photo-b))}

/* back cover */
.back-copy{position:absolute;left:26px;top:30px;width:378px;font-size:7.6px;line-height:1.35}
.back-copy p{margin-bottom:6px}
.endorse{margin-bottom:6px}
.endorse .who{display:block;color:var(--orange);font-style:italic;font-weight:600}
.endorse .role{display:block;color:var(--orange);font-style:italic;font-size:7px}
.back-copy .short{width:220px}
.portrait{left:212px;top:318px;width:206px;height:226px;background:radial-gradient(ellipse at 50% 35%,#5a544b,#2a2824 70%,transparent 100%)}
.stores{position:absolute;left:28px;top:450px;display:flex;gap:5px}
.badge{background:#fff;color:#111;font:700 6.5px "Roboto Condensed",sans-serif;padding:4px 5px;border-radius:2px;line-height:1.1;text-align:center}
.badge small{display:block;font-weight:400;font-size:5px}
.badge--dark{background:#111;color:#fff;border:1px solid #666}
.badge--brightwell{display:flex;align-items:center;gap:3px;background:transparent;color:#fff}
.badge--brightwell i{width:9px;height:9px;border-radius:50%;background:var(--text);display:block}
.badge--blue{background:#2a7fd4;color:#fff}
.partners{position:absolute;left:28px;top:482px;display:flex;align-items:center;gap:14px}
.partner-shape{width:24px;height:24px;border-radius:50%;background:#5a5a5a}
.partner-name{font:700 15px "Roboto Condensed",sans-serif;color:#fff}
.email{position:absolute;left:216px;top:500px;font:400 7.5px "Roboto Condensed",sans-serif;color:#fff;display:flex;align-items:center;gap:4px}
.social{position:absolute;left:28px;top:512px;display:flex;gap:3px}
.social span{width:9px;height:9px;background:var(--orange);border-radius:1px}
.web{position:absolute;left:28px;top:527px;font:400 8.5px "Roboto Condensed",sans-serif;color:#fff;display:flex;align-items:center;gap:4px}

/* front cover */
.cover-photo{left:24px;top:24px;width:382px;height:380px;background:linear-gradient(180deg,#55524b 0%,#3a3731 45%,#1d1c1a 100%)}
.cover-inner-frame{position:absolute;left:40px;top:34px;width:350px;height:370px;border:1px solid var(--frame)}
.release{position:absolute;left:98px;top:30px;display:flex;font:700 8px "Roboto Condensed",sans-serif}
.release .tag{background:var(--orange);color:#111;padding:3px 6px}
.release .list{background:#fff;color:#1b5fa8;padding:3px 6px}
.cover-title{position:absolute;left:0;width:430px;top:232px;text-align:center;font:700 60px/1 "Oswald",sans-serif;letter-spacing:1px;color:var(--gold);text-shadow:0 2px 4px rgba(0,0,0,.6)}
.cover-sub{position:absolute;left:0;width:430px;top:302px;text-align:center;font:400 19px/1.15 "Crimson Text",serif;color:#ece6da}
.cover-sub em{display:block;color:var(--gold)}
.cover-author{position:absolute;left:0;width:430px;top:452px;text-align:center;font:400 25px "Roboto Condensed",sans-serif;letter-spacing:3px;color:#e6e1d8}
.cover-with{position:absolute;left:0;width:430px;top:486px;text-align:center;font:400 11px "Roboto Condensed",sans-serif;letter-spacing:1.5px;color:#e6e1d8}

/* inside left */
.excerpt-head{position:absolute;left:0;width:430px;top:28px;text-align:center;font:400 40px/1 "Black Ops One",sans-serif;color:var(--orange)}
.excerpt-sub{position:absolute;left:0;width:430px;top:74px;text-align:center;font:italic 400 14px/1.1 "Crimson Text",serif;color:#fff}
.excerpt-sub em{display:block;color:var(--orange)}
.excerpt{position:absolute;left:28px;top:112px;width:374px;font-size:8.2px;line-height:1.34}
.excerpt p{margin-bottom:6px}
.excerpt p.lead::first-letter{font-size:20px;float:left;line-height:.9;margin-right:2px;color:#fff}
.book-thumb{float:right;width:74px;height:106px;margin:2px 0 4px 10px;background:linear-gradient(180deg,#4a463f,#141312);border:1px solid #555;position:relative}
.book-thumb b{position:absolute;left:0;right:0;top:52px;text-align:center;font:700 13px "Oswald",sans-serif;color:var(--gold)}
.principles{list-style:none;margin:0 0 6px 14px}
.principles li::before{content:"•";margin-right:4px}

/* inside right */
.acro-head{position:absolute;left:24px;top:30px;width:382px;font:italic 700 13.5px "Roboto Condensed",sans-serif;color:var(--orange)}
.praise{position:absolute;left:28px;top:54px;width:374px;font-size:8px;line-height:1.34}
.praise .endorse{margin-bottom:7px}
.praise .narrow{width:230px}
.praise em{color:var(--orange)}
.couple{left:200px;top:248px;width:218px;height:296px;background:radial-gradient(ellipse at 55% 40%,#4d4a45,#24221f 65%,transparent 100%)}
.hof-badge{position:absolute;left:190px;top:322px;width:54px;height:36px;background:#e9e4dc;border-radius:3px}
.pull-quote{position:absolute;left:30px;top:358px;width:188px;font:italic 400 8.4px/1.32 "Crimson Text",serif;color:var(--text)}
.pull-quote .mark{font:700 20px/0 "Crimson Text",serif;color:var(--orange);vertical-align:-6px;margin-right:2px}
</style>
</head>
<body>

<!-- OUTSIDE SPREAD: back cover + front cover -->
<section class="spread spread--outside">
  <article class="page page--back">
    <div class="frame"></div>
    <div class="back-copy">
      <p>Many of us would say it takes guts and a little bit of crazy to step toe-to-toe with a powerful, 1,500 pound bull. For Hall-of-Fame bullfighter Dalton Prewitt, it took faith.</p>
      <p>Prewitt's remarkable and illustrious journey began at a young age when he received a God-given calling to become a professional bullfighter. Soon after accepting a rodeo scholarship, he suffered a near-fatal electric shock, yet he kept his faith and fought his way back into the arena to live out his calling.</p>
      <p>Once a small town kid from the Ozarks, now a Hall-of-Fame cowboy, Prewitt is sharing his stories of strength and service. With God at the center of this fascinating story, Ride Onward highlights the ten biblical principles that Prewitt learned, experienced, and lived by as a bullfighter, officer and follower of Jesus Christ.</p>
      <div class="endorse">"Ride Onward is the inspirational story of a tough and faith-based cowboy who shows us that 'walking the walk' is a way of life in rodeo, love, and faith."
        <span class="who">R.J. Calder</span><span class="role">No. 1 Daily Ledger Bestselling Author</span></div>
      <div class="endorse">"Whether serving his country, fighting bulls, or raising his family, Dalton Prewitt proves that, with God, the possibilities are endless."
        <span class="who">Ned Hargrove</span><span class="role">Former Secretary of State</span></div>
      <div class="endorse short">"Dalton's journey is uplifting and inspiring! In Ride Onward, he shows how faith can carry us along any path."
        <span class="who">Cole Barrett</span><span class="role">Seven-time World Champion Team Roper</span></div>
      <div class="endorse short">"Dalton Prewitt witnesses to the rawness of rodeo bullfighting and the reality of God's calling on his life."
        <span class="who">Martin L. Avery</span><span class="role">Major General (Retired)</span></div>
      <div class="endorse short">"Ride Onward is an honest look at courage, struggle and the determination to follow his dream under God's lead."
        <span class="who">Duane Kessler</span><span class="role">World Champion Bullfighter</span></div>
    </div>
    <div class="photo portrait" role="img" aria-label="Portrait of the author in a white cowboy hat and plaid shirt"></div>
    <div class="stores">
      <div class="badge"><small>Pre-order at</small>Hartley &amp; Crane</div>
      <div class="badge badge--dark"><small>Pre-order on</small>Velmora</div>
      <div class="badge badge--brightwell"><i></i>Brightwell</div>
      <div class="badge badge--blue">Pages Galore</div>
    </div>
    <div class="partners">
      <div class="partner-shape"></div>
      <div class="partner-name">Tumbleford</div>
    </div>
    <div class="email">
      <svg width="10" height="7" viewBox="0 0 10 7"><rect x="0.5" y="0.5" width="9" height="6" fill="var(--orange)"/><path d="M0.5 0.5 5 4 9.5 0.5" fill="none" stroke="#111" stroke-width="0.8"/></svg>
      dprewitt07@mailnest.example
    </div>
    <div class="social"><span></span><span></span><span></span><span></span></div>
    <div class="web">
      <svg width="9" height="9" viewBox="0 0 10 10"><circle cx="5" cy="5" r="4.3" fill="none" stroke="var(--orange)" stroke-width="1"/><path d="M0.7 5h8.6M5 0.7c-2.4 2.8-2.4 5.8 0 8.6M5 0.7c2.4 2.8 2.4 5.8 0 8.6" fill="none" stroke="var(--orange)" stroke-width="0.8"/></svg>
      www.daltonprewitt.example
    </div>
  </article>

  <article class="page page--front">
    <div class="frame"></div>
    <div class="photo cover-photo" role="img" aria-label="Bullfighter in a white hat facing a charging bull in the rodeo arena"></div>
    <div class="cover-inner-frame"></div>
    <div class="release"><span class="tag">#1 New Release</span><span class="list">in Rodeo</span></div>
    <h1 class="cover-title">RIDE ONWARD</h1>
    <p class="cover-sub">10 Principles that Guided<em>My Cowboy Journey</em></p>
    <p class="cover-author">DALTON PREWITT</p>
    <p class="cover-with">WITH WADE HOLLOWAY</p>
  </article>
</section>

<!-- INSIDE SPREAD: excerpt + endorsements -->
<section class="spread spread--inside">
  <article class="page page--excerpt">
    <div class="frame"></div>
    <h2 class="excerpt-head">RIDE ONWARD</h2>
    <p class="excerpt-sub">10 Principles that Guided<em>My Cowboy Journey</em></p>
    <div class="excerpt">
      <p class="lead">This is the story of my cowboy journey and the principles that carried me along the way. While some are Biblical truths instilled by my parents, others were learned while pursuing my dream. Unfortunately, it took drifting off the beaten path from time to time to truly understand their importance.</p>
      <p>I believe they are foundational in any journey, whether you're fighting bulls in a rodeo, navigating bull-headed coworkers over office politics, or trying to wrangle mischievous teenagers.</p>
      <div class="book-thumb" role="img" aria-label="Book cover thumbnail"><b>RIDE ONWARD</b></div>
      <p>These are the principles I'll unpack as I share my story, and I believe they'll serve you well as you respond to God's call on your life—whatever it is and however He speaks to you:</p>
      <ul class="principles">
        <li>Lend a Hand—Exhortation can change a life.</li>
        <li>Step Through—Faith makes all things possible.</li>
        <li>Beat Down—The hard work of preparation never ends.</li>
        <li>Shoot the Gap—To sacrifice is to live.</li>
        <li>EGO (Edging God Out)—Humility is a true reflection of strength.</li>
        <li>Cowboy Up—Know your priorities.</li>
        <li>The Razor—Confidence is a fine line.</li>
        <li>The Gold Buckle—Integrity can't be bought.</li>
        <li>Find Your Spotter—Listen to smart people.</li>
        <li>Turn 'Em Out—Restoration leads to fulfillment.</li>
      </ul>
      <p>I was an ordinary kid who eventually lived out my passion for the Western way of life and a God-given vision by becoming a professional bullfighter. So I'm living proof that even a small-town kid has big-time potential.</p>
      <p>The road wasn't straight and the path wasn't easy. Along the way, I overcame the near-death experience from that electrical shock; suffered multiple concussions from too-close encounters with bulls; and endured a bitter divorce and international child-custody battle. I looked fear in the eyes and refused to blink, proudly serving in the military following the terrorist attacks on 9/11. And, eventually, I became the youngest cowboy enshrined in the Sagebrush Frontier Days Hall of Fame.</p>
      <p>Through all of the highs and lows, these principles guided me along my cowboy journey. They never let me down…when I applied them. So I hope by sharing my story, you can learn from my mistakes and successes and apply these principles to your life. Because if God can use me, I know He can use you!</p>
    </div>
  </article>

  <article class="page page--praise">
    <div class="frame"></div>
    <h2 class="acro-head">Rise, Observe, Nurture, Aid, Rejoice, &amp; Dedicate</h2>
    <div class="praise">
      <div class="endorse">"Dalton Prewitt has done what few before him have—served his country while still responding to God's call to <em>Ride Onward—Rising, Observing, Nurturing, Aiding, Rejoicing and Dedicating</em>—as a rodeo bullfighter. Ride Onward will leave readers with a strong conviction to follow God's lead."
        <span class="who">Carl Brennick</span><span class="role">Commissioner, Pro Rodeo Riders League</span></div>
      <div class="endorse">"Ride Onward is a remarkable true story of a man with faith that overcomes the obstacles of life and makes a difference in the world around him!"
        <span class="who">Clint Ashby Rowe</span><span class="role">Seven-time World Champion Team Roper</span></div>
      <div class="endorse narrow">"If you want to be a champion in life, Ride Onward is the book for you. I encourage all to read Dalton's incredible journey in discovering his true calling."
        <span class="who">Sam Medeiros</span><span class="role">World Champion Bull Rider</span></div>
      <div class="endorse narrow">"Dalton Prewitt made a commitment to serve his country, and made a commitment to himself to serve God. His 10 principles can help anyone struggling with personal and professional balance. Ride Onward is a must-read for us all."
        <span class="who">Flynn Rasmund</span><span class="role">Premier Bull Riders Exclusive Entertainer</span></div>
    </div>
    <div class="photo couple" role="img" aria-label="The author standing with his wife at the Hall of Fame ceremony"></div>
    <div class="hof-badge" role="img" aria-label="Hall of Fame badge"></div>
    <p class="pull-quote"><span class="mark">“</span>Soon after accepting Jesus Christ into his life, Dalton Prewitt received a specific vision from God. At 14, God called Dalton to be a rodeo bullfighter. He went on to become a professional bullfighter and was later enshrined in the Sagebrush Frontier Days Rodeo Hall of Fame. Dalton earned his MBA and served his country as an officer, where he was endorsed as the only professional bullfighter in the history of his branch. Dalton and wife, Janie, live in Hollins Ridge with their beautiful twin boys.<span class="mark">”</span></p>
  </article>
</section>

</body>
</html>
```